Land Buying Company Needs Letterhead for Direct Mail Marketing to Land Owners

We are looking for a professional letterhead that we will be including in our direct mail marketing. We will be sending this to land owners who may be interested in selling or purchasing land.

The letterhead needs to be editable. Headers and footers would look nice, but we are open. We would want it to include our address, website, phone, and email info. For right now the address to use for design purposes would the following:

Address: 415 Bramwell Avenue #600
Dallas, TX 75219
Website - www.quillridgeacres.example
Email - info@quillridgeacres.example
Phone - 866-402-ACRE

I have attached our logo zip file that we just had done on Pixel Guild. Let me know what questions you have, and thank you.

```html
<!DOCTYPE html>
<html lang="en">
<head>
<meta charset="utf-8">
<title>Quillridge Acres Letterhead</title>
<link rel="stylesheet" href="https://fonts.googleapis.com/css2?family=Lato:wght@400&family=Montserrat:wght@700&display=swap">
<style>
  :root {
    --backdrop: #9a9a9a;
    --paper: #e6e6e6;
    --forest: #465a1f;
    --leaf: #8cc63f;
    --ink: #1e1e1e;
    --footer-text: #ececec;
    --rule-dark: #8a8a8a;
    --rule-light: #d6d6d6;
  }
  * { margin: 0; padding: 0; box-sizing: border-box; }
  html, body {
    width: 1200px;
    height: 900px;
    overflow: hidden;
    background: var(--backdrop);
  }
  .letterhead {
    position: absolute;
    left: 267px;
    top: 20px;
    width: 665px;
    height: 860px;
    background: var(--paper);
  }
  .brand {
    position: absolute;
    left: 52px;
    top: 42px;
    display: flex;
    align-items: center;
    gap: 14px;
  }
  .brand-dot {
    width: 58px;
    height: 58px;
    border-radius: 50%;
    background: var(--forest);
  }
  .brand-name {
    font-family: "Montserrat", sans-serif;
    font-weight: 700;
    font-size: 27px;
    letter-spacing: 1px;
    text-transform: uppercase;
    color: var(--leaf);
  }
  .contact-list {
    position: absolute;
    left: 502px;
    top: 34px;
    list-style: none;
    font-family: "Lato", sans-serif;
    font-size: 10px;
    line-height: 14.5px;
    color: var(--ink);
  }
  .contact-list li {
    display: flex;
    align-items: center;
    gap: 3px;
    white-space: nowrap;
  }
  .contact-icon { width: 10px; height: 10px; flex: none; }
  .footer-band {
    position: absolute;
    left: 0;
    bottom: 0;
    width: 665px;
    height: 70px;
  }
  .footer-address {
    position: absolute;
    left: 246px;
    top: 808px;
    font-family: "Lato", sans-serif;
    font-size: 18.5px;
    color: var(--footer-text);
    white-space: nowrap;
  }
</style>
</head>
<body>
  <main class="letterhead">
    <header class="brand">
      <div class="brand-dot"></div>
      <div class="brand-name">Quillridge Acres</div>
    </header>

    <ul class="contact-list">
      <li>
        <svg class="contact-icon" viewBox="0 0 10 10"><circle cx="5" cy="5" r="4.3" fill="none" stroke="#465a1f" stroke-width="1"/><path d="M3.3 2.8l1 1-.5.7a3.5 3.5 0 0 0 1.7 1.7l.7-.5 1 1-.8.7c-2 0-3.8-1.8-3.8-3.8z" fill="#465a1f"/></svg>
        866-402-ACRE
      </li>
      <li>
        <svg class="contact-icon" viewBox="0 0 10 10"><rect x="0.6" y="2" width="8.8" height="6" fill="none" stroke="#465a1f" stroke-width="0.9"/><path d="M0.8 2.2L5 5.6l4.2-3.4" fill="none" stroke="#465a1f" stroke-width="0.9"/></svg>
        info@quillridgeacres.example
      </li>
      <li>
        <svg class="contact-icon" viewBox="0 0 10 10"><circle cx="5" cy="5" r="4.3" fill="none" stroke="#465a1f" stroke-width="1"/><path d="M0.8 5h8.4M5 0.8c-2.2 2.4-2.2 6 0 8.4M5 0.8c2.2 2.4 2.2 6 0 8.4" fill="none" stroke="#465a1f" stroke-width="0.8"/></svg>
        www.quillridgeacres.example
      </li>
    </ul>

    <svg class="footer-band" viewBox="0 0 665 70" aria-hidden="true">
      <defs>
        <linearGradient id="rule-sheen" x1="0" x2="1" y1="0" y2="0">
          <stop offset="0" stop-color="#8a8a8a"/>
          <stop offset="0.45" stop-color="#d6d6d6"/>
          <stop offset="1" stop-color="#8a8a8a"/>
        </linearGradient>
      </defs>
      <rect x="0" y="7" width="180" height="53" fill="#465a1f"/>
      <rect x="177" y="6" width="488" height="41" fill="#465a1f"/>
      <rect x="205" y="51" width="460" height="8" fill="url(#rule-sheen)"/>
      <circle cx="177" cy="33" r="33" fill="#e6e6e6"/>
      <circle cx="177" cy="33" r="29" fill="#465a1f"/>
    </svg>
    <p class="footer-address">415 Bramwell Avenue #600 Dallas, TX 75219</p>
  </main>
</body>
</html>
```